依頼詳細
ゴミ屋敷の片づけ・遺品整理等の事業になります。
ポスティングを想定しています。
ターゲットは高齢者になりますのでわかりやすいデザインでお願いします。
記載項目
屋号:そよかぜクリーンサービス
電話番号:未定
サイズ
A4
ページ数
両面
希望イメージ
シンプル 複雑
単色 カラフル
暗い 明るい
日常 高級
遊び心 厳粛
未来的 伝統的
女性的 男性的
希望する色
緑系
納品ファイル
• 高解像度JPG (.jpg)
補足説明
■ 選んだ理由

高齢者向けということでイラストを多用しわかりやすいデザインで気に入りました。
ベースもやさしめの色合いで好きです。

■ 提案者全員のお礼・コメント

さまざまな提案をいただき感謝しています。ありがとうございました。

```html
<!DOCTYPE html>
<html lang="ja">
<head>
<meta charset="UTF-8">
<title>そよかぜクリーンサービス チラシ</title>
<link href="https://fonts.googleapis.com/css2?family=M+PLUS+Rounded+1c:wght@500;700;800;900&family=Noto+Sans+JP:wght@400;700;900&display=swap" rel="stylesheet">
<style>
:root{
  --green:#3fa535;
  --green-dark:#22802a;
  --green-pale:#e6f3dc;
  --sky:#dcedf6;
  --red:#e6312d;
  --red-tag:#e34b5a;
  --blue-tag:#3e8fd0;
  --orange-tag:#f08a24;
  --purple-tag:#8f6bb8;
  --ink:#2b2b2b;
  --white:#ffffff;
}
*{margin:0;padding:0;box-sizing:border-box}
html,body{width:848px;height:1200px;overflow:hidden;background:#fff}
body{font-family:"M PLUS Rounded 1c","Noto Sans JP",sans-serif;color:var(--ink)}
.flyer{position:relative;width:848px;height:1200px;background:linear-gradient(180deg,var(--sky) 0,#f4f9fc 420px,#fff 460px);overflow:hidden}
.tag{position:absolute;top:18px;background:var(--green);color:#fff;font-weight:900;font-size:24px;padding:6px 18px;border-radius:6px}
.tag--left{left:18px}
.tag--right{right:18px}
.staff-art{position:absolute;left:300px;top:60px;width:460px;height:280px;border-radius:30px;background:radial-gradient(circle at 50% 40%,#fbe3c8 0,#cfe3f1 55%,#b9d7ea 100%)}
.lead{position:absolute;left:130px;top:190px;font-weight:900;color:var(--ink);line-height:1.35}
.lead .l1{font-size:30px;color:var(--red)}
.lead .l2{font-size:32px}
.lead .hl{color:var(--red);background:linear-gradient(transparent 60%,#fff27a 60%)}
.banner{position:absolute;left:0;top:290px;width:848px;height:180px}
.banner-text{position:absolute;left:0;width:848px;text-align:center;font-weight:900}
.banner-sub{top:300px;font-size:22px;color:var(--green-dark)}
.banner-name{top:332px;font-size:54px;color:#fff;letter-spacing:2px}
.banner-tail{top:412px;font-size:40px;color:var(--green-dark)}
.services{position:absolute;left:18px;top:478px;width:812px;display:grid;grid-template-columns:1fr 1fr;gap:10px 12px}
.service{display:flex;border:2px solid #d5d5d5;border-radius:6px;background:#fff;height:104px;overflow:hidden}
.service-label{width:120px;flex:none;color:#fff;font-weight:900;font-size:19px;display:flex;align-items:center;justify-content:center;text-align:center;line-height:1.25;padding:4px}
.service-text{padding:8px 10px;font-family:"Noto Sans JP",sans-serif;font-size:15px;line-height:1.45;font-weight:700}
.service-text em{font-style:normal;color:var(--red)}
.c-green{background:var(--green)}.c-red{background:var(--red-tag)}.c-blue{background:var(--blue-tag)}.c-orange{background:var(--orange-tag)}.c-purple{background:var(--purple-tag)}
.operator-art{position:absolute;left:26px;top:846px;width:150px;height:140px;border-radius:20px;background:linear-gradient(160deg,#f6d7b8,#f2b37d)}
.bubble{position:absolute;left:20px;top:990px;width:170px;font-size:12px;font-weight:700;line-height:1.4;background:#fff;border:1.5px solid var(--orange-tag);border-radius:10px;padding:6px 8px}
.contact{position:absolute;left:210px;top:852px;width:620px;font-weight:900}
.contact .c1{font-size:28px}
.contact .c2{font-size:34px;margin-top:6px}
.contact .c3{font-size:34px;margin-top:2px}
.contact .red{color:var(--red)}
.phone{position:absolute;left:206px;top:980px;width:624px;display:flex;align-items:center;gap:10px}
.phone-icon{width:58px;height:58px;border-radius:8px;background:var(--red);display:flex;align-items:center;justify-content:center}
.phone-num{font-family:"Noto Sans JP",sans-serif;font-weight:900;font-size:62px;color:var(--red);letter-spacing:1px;line-height:1}
.hours{position:absolute;left:470px;top:1048px;font-size:15px;font-weight:700}
.footer{position:absolute;left:0;top:1072px;width:848px;height:128px;background:var(--green-pale);border-top:4px solid var(--green)}
.footer-name{position:absolute;left:18px;top:12px;font-size:44px;font-weight:900;color:var(--green-dark)}
.footer-cards{position:absolute;left:20px;top:76px;display:flex;align-items:center;gap:8px;font-size:18px;font-weight:900}
.card{width:42px;height:28px;border-radius:4px;background:#9bb8d3}
.card:nth-child(3){background:#e8a15a}.card:nth-child(4){background:#8ab27c}.card:nth-child(5){background:#b19ac9}
.footer-company{position:absolute;right:24px;top:20px;font-family:"Noto Sans JP",sans-serif;font-size:15px;font-weight:700;line-height:1.6;text-align:left}
</style>
</head>
<body>
<main class="flyer">
  <div class="tag tag--left">完全保存版!</div>
  <div class="tag tag--right">必ずお役にたちます!</div>
  <div class="staff-art" role="img" aria-label="作業着姿で笑顔のスタッフ二人のイラスト"></div>

  <div class="lead">
    <div class="l1">暮らしの</div>
    <div class="l2"><span class="hl">「困った!」</span>は…</div>
  </div>

  <svg class="banner" viewBox="0 0 848 180" aria-hidden="true">
    <path d="M60 70 Q424 -10 788 70 L788 130 Q424 50 60 130 Z" fill="var(--green)"/>
    <path d="M60 70 Q424 -10 788 70" fill="none" stroke="#fff" stroke-width="3"/>
  </svg>
  <div class="banner-text banner-sub">～新潟県請負人～</div>
  <div class="banner-text banner-name">そよかぜクリーンサービス</div>
  <div class="banner-text banner-tail">にお任せください!</div>

  <section class="services">
    <div class="service"><div class="service-label c-green">暮らしの<br>お片付け</div><div class="service-text"><em>ゴミ屋敷をピカピカに!</em>ベランダのお掃除!不用品の処分!</div></div>
    <div class="service"><div class="service-label c-red">遺品の<br>整理</div><div class="service-text">思い出が詰まった大切な遺品、当社が丁寧に整理致します。その他遺品に関するお悩みご相談承ります。</div></div>
    <div class="service"><div class="service-label c-blue">トランクルームの<br>お片付け</div><div class="service-text">お荷物を指定の場所までお運びします!もちろん不用品も処分OK!</div></div>
    <div class="service"><div class="service-label c-orange">高価買取</div><div class="service-text">ただ処分するだけではありません!まだ使える家具・貴金属等高価買取致します!ご相談ください!</div></div>
    <div class="service"><div class="service-label c-purple">リフォーム</div><div class="service-text">遺品整理後の壁紙修繕から床の張替・エアコン取付けなど!小さなことから大きなことまでご相談を!</div></div>
    <div class="service"><div class="service-label c-purple">電気の困った</div><div class="service-text">エアコンの取外しやウォシュレットの交換など電気の困ったもご相談ください!</div></div>
  </section>

  <div class="operator-art" role="img" aria-label="電話対応をする女性スタッフのイラスト"></div>
  <div class="bubble">どんなことでもお気軽にご相談ください!お待ちしております。</div>

  <div class="contact">
    <div class="c1">お部屋をキレイに!毎日を快適に!</div>
    <div class="c2">まずは<span class="red">お電話</span>でお見積を!</div>
    <div class="c3">よろしければ<span class="red">その日</span>にお伺いします。</div>
  </div>
  <div class="phone">
    <div class="phone-icon">
      <svg width="36" height="36" viewBox="0 0 24 24" aria-hidden="true"><path fill="#fff" d="M6.6 10.8a15 15 0 0 0 6.6 6.6l2.2-2.2a1 1 0 0 1 1-.25 11.4 11.4 0 0 0 3.6.57 1 1 0 0 1 1 1V20a1 1 0 0 1-1 1A17 17 0 0 1 3 4a1 1 0 0 1 1-1h3.5a1 1 0 0 1 1 1c0 1.25.2 2.45.57 3.57a1 1 0 0 1-.25 1z"/></svg>
    </div>
    <div class="phone-num">000-000-0000</div>
  </div>
  <div class="hours">(お電話受付)AM9:00～PM8:00 定休日:日曜日</div>

  <footer class="footer">
    <div class="footer-name">そよかぜクリーンサービス</div>
    <div class="footer-cards">各種クレジットカードOK!!
      <span class="card"></span><span class="card"></span><span class="card"></span><span class="card"></span>
    </div>
    <div class="footer-company">(株)みどりのわ<br>〒150-0000<br>東京都みどり区そよ町1-2-3</div>
  </footer>
</main>
</body>
</html>
```